KTNW Unique Letterhead for Financial Services Business

I am looking for a letterhead design to match our branding colours. I do not want to see anything generic that could be created in word, I can do that myself, I am after something with a bit of designer flair. Once completed I will need files in a print ready format (including bleed area).

I have included our logo file and also our new business card design but get creative.

Industry/Entity Type

Financial Services

Font styles to use
Other font styles liked:
• raleway

Colors
00AB8E
00BBA5
67D7C9
C6EFE9
E9F9F6

Requirements
Must have
• Must be consisten with logo branding colours.
Should not have
• Anything generic that I could create myself in word

```html
<!DOCTYPE html>
<html lang="en">
<head>
<meta charset="UTF-8">
<title>KTNW Letterhead</title>
<link rel="stylesheet" href="https://fonts.googleapis.com/css2?family=Montserrat:ital,wght@0,400;0,600;0,700;1,400&family=Poppins:ital,wght@0,400;0,600;1,400&display=swap">
<style>
  :root {
    --backdrop: #e4e6e7;
    --paper: #ffffff;
    --ink: #1e1e1e;
    --brand-green: #00AB8E;
    --brand-teal: #00BBA5;
    --brand-aqua: #67D7C9;
    --brand-mint: #C6EFE9;
    --brand-frost: #E9F9F6;
    --brand-deep: #00876f;
    --header-text: #ffffff;
  }
  * { box-sizing: border-box; margin: 0; padding: 0; }
  html, body { width: 1200px; height: 920px; overflow: hidden; }
  body { background: var(--backdrop); position: relative; font-family: "Montserrat", sans-serif; color: var(--ink); }

  .letterhead {
    position: absolute; left: 288px; top: 20px;
    width: 624px; height: 880px;
    background: var(--paper);
    box-shadow: 0 6px 18px rgba(0,0,0,0.18);
    overflow: hidden;
  }

  .header { position: absolute; left: 0; top: 0; width: 624px; height: 140px; }
  .header-shapes { position: absolute; inset: 0; }

  .brand { position: absolute; left: 38px; top: 62px; display: flex; align-items: center; gap: 10px; }
  .brand-square { width: 26px; height: 26px; background: var(--brand-green); }
  .brand-name { font-family: "Montserrat", sans-serif; font-weight: 400; font-size: 34px; letter-spacing: 4px; color: var(--brand-green); line-height: 1; }

  .contact { position: absolute; right: 28px; top: 20px; text-align: right; color: var(--header-text); font-family: "Poppins", sans-serif; }
  .contact-name { font-weight: 600; font-size: 14.5px; letter-spacing: 0.2px; line-height: 18px; }
  .contact-role { font-style: italic; font-size: 7.5px; line-height: 12px; }
  .contact-lines { margin-top: 14px; font-size: 9.5px; line-height: 11.3px; }
  .contact-lines li { list-style: none; display: flex; justify-content: flex-end; align-items: center; gap: 6px; }
  .contact-lines svg { width: 6px; height: 6px; fill: var(--header-text); }
  .contact-rule { position: absolute; right: 28px; top: 110px; width: 209px; height: 1px; background: rgba(255,255,255,0.75); }
  .contact-address { position: absolute; right: 28px; top: 115px; font-family: "Poppins", sans-serif; font-size: 8px; color: var(--header-text); }

  .watermark-symbol {
    position: absolute; left: 330px; top: 530px; width: 294px; height: 335px;
    background: radial-gradient(ellipse at 70% 55%, rgba(198,239,233,0.75), rgba(233,249,246,0.35) 60%, rgba(255,255,255,0) 80%);
  }

  .letter { position: absolute; left: 58px; top: 204px; width: 514px; font-size: 10.1px; line-height: 13.8px; letter-spacing: -0.12px; }
  .letter-opening { margin-bottom: 13.8px; }
  .letter p.body { text-align: justify; margin-bottom: 13.8px; }

  .signoff { position: absolute; left: 56px; top: 634px; font-size: 10.1px; }
  .signature-mark { position: absolute; left: 78px; top: 650px; width: 92px; height: 62px; background: linear-gradient(135deg, rgba(0,171,142,0.10), rgba(233,249,246,0.4)); }
  .signer { position: absolute; left: 56px; top: 720px; font-size: 10.6px; font-weight: 700; }

  .footer-band { position: absolute; left: 0; bottom: 2px; width: 624px; height: 11px; background: linear-gradient(90deg, var(--brand-mint), var(--brand-aqua) 35%, var(--brand-green)); }
</style>
</head>
<body>
<main class="letterhead">
  <header class="header">
    <svg class="header-shapes" viewBox="0 0 624 140" preserveAspectRatio="none">
      <defs>
        <linearGradient id="panelFill" x1="0" y1="0" x2="1" y2="0">
          <stop offset="0" stop-color="#00BBA5"/>
          <stop offset="0.5" stop-color="#00AB8E"/>
          <stop offset="1" stop-color="#00876f"/>
        </linearGradient>
        <linearGradient id="chevronFill" x1="0" y1="0" x2="0" y2="1">
          <stop offset="0" stop-color="#00AB8E"/>
          <stop offset="1" stop-color="#00876f"/>
        </linearGradient>
      </defs>
      <polygon points="260,0 300,0 352,90 314,140 294,140 338,88" fill="url(#chevronFill)"/>
      <polygon points="292,0 624,0 624,140 316,140 352,90" fill="url(#panelFill)"/>
      <polygon points="292,0 304,0 352,90 344,100" fill="#C6EFE9" opacity="0.85"/>
    </svg>
    <div class="brand">
      <span class="brand-square"></span>
      <span class="brand-name">KTNW</span>
    </div>
    <div class="contact">
      <div class="contact-name">NAME GOES HERE</div>
      <div class="contact-role">Designation Goes here</div>
      <ul class="contact-lines">
        <li>+0123 456 789 <svg viewBox="0 0 10 10"><path d="M2 0h2l1 3-1.5 1a6 6 0 0 0 2.5 2.5L7 5l3 1v2c0 1-1 2-2 2A8 8 0 0 1 0 2c0-1 1-2 2-2z"/></svg></li>
        <li>info@yourmailid.com <svg viewBox="0 0 10 10"><rect x="0" y="2" width="10" height="6"/></svg></li>
        <li>www.yourwebsite.com <svg viewBox="0 0 10 10"><circle cx="5" cy="5" r="4.5"/></svg></li>
      </ul>
    </div>
    <div class="contact-rule"></div>
    <div class="contact-address">123, your company address goes here, Pin 123456</div>
  </header>

  <div class="watermark-symbol" role="img" aria-label="Faint brand symbol decoration"></div>

  <section class="letter">
    <p class="letter-opening">Lorem Ipsum is simply</p>
    <p class="body">Dummy text of the printing and typesetting industry. Lorem Ipsum has been the industry's standard dummy text ever since the 1500s, when an unknown printer took a galley of type and scrambled it to make a type specimen book. It has survived not only five centuries, but also the leap into electronic typesetting, remaining essentially unchanged. It was popularised in the 1960s with the release of Letraset sheets containing Lorem Ipsum passages, and more recently with desktop publishing software like Aldus PageMaker including versions of Lorem Ipsum.</p>
    <p class="body">Lorem Ipsum is simply dummy text of the printing and typesetting industry. Lorem Ipsum has been the industry's standard dummy text ever since the 1500s, when an unknown printer took a galley of type and scrambled it to make a type specimen book. It has survived not only five centuries, but also the leap into electronic typesetting, remaining essentially unchanged. It was popularised in the 1960s with the release of Letraset sheets containing Lorem Ipsum passages, and more recently with desktop publishing software like Aldus PageMaker including versions of Lorem Ipsum.</p>
    <p class="body">Lorem Ipsum is simply dummy text of the printing and typesetting industry. Lorem Ipsum has been the industry's standard dummy text ever since the 1500s, when an unknown printer took a galley of type and scrambled it to make a type specimen book. It has survived not only five centuries, but also the leap into electronic typesetting, remaining essentially unchanged. It was popularised in the 1960s with the release of Letraset sheets containing Lorem Ipsum passages, and more recently with desktop publishing software like Aldus PageMaker including versions of Lorem Ipsum.</p>
    <p class="body">Lorem Ipsum is simply dummy text of the printing and typesetting industry. Lorem Ipsum has been the industry's standard dummy text ever since the 1500s, when an unknown printer took a galley of type and scrambled it to make a type specimen book. It has survived not only five centuries, but also the leap into electronic typesetting, remaining essentially unchanged.</p>
  </section>

  <p class="signoff">Lorem Ipsum Dummy Text</p>
  <div class="signature-mark" role="img" aria-label="Handwritten signature"></div>
  <p class="signer">Lorem Ipsum Dummy Text</p>

  <div class="footer-band"></div>
</main>
</body>
</html>
```